Wedding Day Custom Wine Label - Tasmanian (Tamar Valley) wine

I am looking for a custom design that will be put on a wine label to commemorate a very good friend's wedding day.

We will need to be able to take the design and print it on to sticker labels that we can put on to wine bottles.

The bride and groom have asked for a simplistic label design (see example image attached). We need two labels. One for "Pinot Noir" wine and the other for "Chardonnay" wine. We would like the label to say:

The Drumwell's
Pinot Noir
2023
Tamar Valley

and for for the other wine variety:

The Drumwell's
Chardonnay
2023
Tamar Valley

smaller text below to say:

13.5% ALC/VOL 750ML
MAREN & JONAS - 31.10.2024

I am happy to consider other variations - the bride & groom would prefer something minimalistic. Elegant and classy.

Target Market(s)

the bride & groom

Requirements
Must have
• Wedding date (31.10.2024). Wine type (Pinot Noir or Chardonnay).
Should not have
• images not essential

```html
<!DOCTYPE html>
<html lang="en">
<head>
<meta charset="utf-8">
<title>The Drumwell's Chardonnay Label</title>
<link rel="stylesheet" href="https://fonts.googleapis.com/css2?family=Barlow+Condensed:wght@300;400&family=Josefin+Sans:wght@300&family=Montserrat:wght@400&display=swap">
<style>
  :root {
    --backdrop: #333333;
    --label-black: #0d0d0e;
    --label-white: #f3f3f3;
    --ink-white: #f2f2f2;
    --gold: #b98331;
    --fine-print: #6a6a6a;
  }
  * { margin: 0; padding: 0; box-sizing: border-box; }
  html, body {
    width: 1200px;
    height: 857px;
    overflow: hidden;
    background: var(--backdrop);
  }
  .canvas {
    position: relative;
    width: 1200px;
    height: 857px;
  }
  .wine-label {
    position: absolute;
    left: 348px;
    top: 69px;
    width: 504px;
    height: 719px;
    display: flex;
    flex-direction: column;
  }
  .label-top {
    position: relative;
    height: 396px;
    background: var(--label-black);
  }
  .family-name {
    position: absolute;
    left: 0;
    right: 0;
    top: 268px;
    text-align: center;
    font-family: "Barlow Condensed", sans-serif;
    font-weight: 300;
    font-size: 30px;
    letter-spacing: 3px;
    color: var(--ink-white);
    text-transform: uppercase;
  }
  .label-band {
    position: relative;
    flex: 1;
    background: var(--label-white);
  }
  .variety {
    position: absolute;
    left: 0;
    right: 0;
    top: 12px;
    text-align: center;
    font-family: "Josefin Sans", sans-serif;
    font-weight: 300;
    font-size: 32px;
    letter-spacing: 19px;
    padding-left: 19px;
    color: var(--gold);
    text-transform: uppercase;
  }
  .vintage {
    position: absolute;
    left: 0;
    right: 0;
    top: 82px;
    display: flex;
    justify-content: center;
    align-items: center;
    gap: 10px;
    font-family: "Barlow Condensed", sans-serif;
    font-weight: 400;
    font-size: 27px;
    color: var(--gold);
  }
  .vintage-rule {
    width: 52px;
    height: 1.5px;
    background: var(--gold);
  }
  .region {
    position: absolute;
    left: 0;
    right: 0;
    top: 110px;
    text-align: center;
    font-family: "Barlow Condensed", sans-serif;
    font-weight: 400;
    font-size: 28px;
    letter-spacing: 1px;
    color: var(--gold);
    text-transform: uppercase;
  }
  .fine-print {
    position: absolute;
    bottom: 40px;
    font-family: "Montserrat", sans-serif;
    font-size: 9px;
    letter-spacing: 0.3px;
    color: var(--fine-print);
    text-transform: uppercase;
  }
  .fine-print--couple { left: 14px; }
  .fine-print--volume { right: 14px; }
</style>
</head>
<body>
  <main class="canvas">
    <article class="wine-label">
      <section class="label-top">
        <h1 class="family-name">The Drumwell's</h1>
      </section>
      <section class="label-band">
        <h2 class="variety">Chardonnay</h2>
        <p class="vintage">
          <span class="vintage-rule"></span>
          <span class="vintage-year">2023</span>
          <span class="vintage-rule"></span>
        </p>
        <p class="region">Tamar Valley</p>
        <p class="fine-print fine-print--couple">Maren &amp; Jonas - 31.10.2024</p>
        <p class="fine-print fine-print--volume">13.5% ALC/VOL 750ML</p>
      </section>
    </article>
  </main>
</body>
</html>
```